Stationery Design Project

We are a packaging machinery manufacturer that mainly serve the food industry.
We now require a full set of stationary including name card, envelop, letter paper, and etc. to match our company image. The logo has been awarded in a previous contest which is attached here.
Updates
Project Deadline Extended
Reason: We have extended the deadline. We have adjusted the deadline before launch to avoid confusion but it turns out the new date wasn't implemented by the system. All designers please feel free to submit your design. Thank you!
Target Market(s)
B2B customer, including decision maker in food factories, chemical factories, etc.
Industry/Entity Type
Industry
Colors
Designer to choose colors to be used in the design.
Look and feel
Each slider illustrates characteristics of the customer's brand and the style your logo design should communicate.

```html
<!DOCTYPE html>
<html lang="en">
<head>
<meta charset="utf-8">
<title>Torvik Stationery Set</title>
<link href="https://fonts.googleapis.com/css2?family=Montserrat:wght@300;400;600&display=swap" rel="stylesheet">
<style>
  :root {
    --green: #0f6a3c;
    --green-dark: #0b5430;
    --green-light: #1d8a52;
    --paper: #f3f4f5;
    --paper-white: #ffffff;
    --ink: #4a4f4c;
    --ink-soft: #8a8f8c;
    --backdrop: #e6e3dc;
    --pattern-grey: #c9cccb;
  }
  * { margin: 0; padding: 0; box-sizing: border-box; }
  html, body { width: 1200px; height: 1096px; overflow: hidden; }
  body {
    background: var(--backdrop);
    font-family: "Montserrat", sans-serif;
    position: relative;
    color: var(--ink);
  }
  .piece { position: absolute; box-shadow: 0 2px 6px rgba(0,0,0,.18); }

  .brand-name { font-weight: 600; letter-spacing: .02em; line-height: 1; display: flex; align-items: center; white-space: nowrap; }
  .brand-square { display: inline-block; margin-right: .22em; flex: none; }
  .brand-tagline { font-weight: 600; letter-spacing: .18em; text-transform: uppercase; line-height: 1; white-space: nowrap; }

  /* Folder */
  .folder { left: 197px; top: 110px; width: 342px; height: 454px; border-radius: 3px 8px 8px 3px; overflow: hidden; }
  .folder-pattern { position: absolute; inset: 0; background: linear-gradient(135deg, var(--green-light) 0%, var(--green) 50%, var(--green-dark) 100%); }
  .folder-brand { position: absolute; left: 12px; top: 178px; color: var(--paper-white); }
  .folder-brand .brand-name { font-size: 62px; }
  .folder-brand .brand-square { width: 48px; height: 48px; background: var(--paper-white); }
  .folder-brand .brand-tagline { font-size: 17px; margin-top: 10px; }

  /* Letterhead */
  .letterhead { left: 594px; top: 258px; width: 319px; height: 449px; background: var(--paper); }
  .letterhead-brand { position: absolute; left: 69px; top: 14px; color: var(--green); }
  .letterhead-brand .brand-name { font-size: 30px; }
  .letterhead-brand .brand-square { width: 22px; height: 22px; background: var(--green); }
  .letterhead-brand .brand-tagline { font-size: 8.5px; margin-top: 4px; }
  .letterhead-rule { position: absolute; left: 69px; top: 60px; width: 187px; height: 1px; background: var(--green); }
  .letter-body { position: absolute; left: 38px; top: 142px; width: 250px; font-size: 6.2px; line-height: 13px; color: var(--ink-soft); text-indent: 20px; }
  .letterhead-footer { position: absolute; left: 0; bottom: 0; width: 100%; height: 40px; background: var(--green); color: var(--paper-white); font-size: 8px; padding: 3px 6px; display: flex; justify-content: space-between; line-height: 11.3px; }
  .letterhead-footer .contact-right { text-align: right; }

  /* Business cards */
  .card-front { left: 401px; top: 631px; width: 138px; height: 76px; overflow: hidden; }
  .card-pattern { position: absolute; inset: 0; background: linear-gradient(180deg, #d6d8d7, var(--pattern-grey)); }
  .card-front-brand { position: absolute; left: 5px; top: 24px; color: var(--green); }
  .card-front-brand .brand-name { font-size: 22px; }
  .card-front-brand .brand-square { width: 17px; height: 17px; background: var(--green); }
  .card-front-brand .brand-tagline { font-size: 6.2px; margin-top: 4px; letter-spacing: .12em; color: var(--ink-soft); }

  .card-back { left: 401px; top: 758px; width: 138px; height: 80px; background: var(--paper-white); text-align: right; padding: 5px 10px 0 0; }
  .card-name { font-size: 12px; font-weight: 300; color: var(--green); text-align: center; padding-left: 10px; }
  .card-role { font-size: 6px; color: var(--ink-soft); text-align: center; padding-left: 10px; margin-bottom: 3px; }
  .card-contact { font-size: 5.6px; line-height: 8px; color: var(--ink); }
  .card-contact b { color: var(--green); font-weight: 600; }

  /* Envelope back */
  .envelope-back { left: 597px; top: 762px; width: 241px; height: 170px; background: var(--paper-white); overflow: hidden; }
  .envelope-flap { position: absolute; left: 0; top: 0; width: 241px; height: 170px; }
  .envelope-band { position: absolute; left: 75px; top: 0; width: 92px; height: 170px; background: var(--green); color: var(--paper-white); }
  .envelope-brand { position: absolute; left: 0; width: 100%; top: 27px; display: flex; flex-direction: column; align-items: center; }
  .envelope-brand .brand-name { font-size: 16px; }
  .envelope-brand .brand-square { width: 12px; height: 12px; background: var(--paper-white); }
  .envelope-brand .brand-tagline { font-size: 5px; margin-top: 3px; letter-spacing: .12em; }
  .envelope-name { position: absolute; left: 10px; top: 140px; font-size: 9px; font-weight: 300; white-space: nowrap; }
  .envelope-role { position: absolute; left: 12px; top: 153px; font-size: 5px; opacity: .8; white-space: nowrap; }

  /* Envelope front */
  .envelope-front { left: 730px; top: 814px; width: 244px; height: 170px; background: var(--paper-white); }
  .envelope-footer { position: absolute; left: 0; bottom: 0; width: 100%; height: 38px; background: var(--green); color: var(--paper-white); font-size: 6px; line-height: 9px; padding: 5px 5px; display: flex; justify-content: space-between; }
  .envelope-footer .contact-right { text-align: right; }
</style>
</head>
<body>

  <section class="piece folder">
    <div class="folder-pattern" role="img" aria-label="Geometric green folding pattern across the folder cover"></div>
    <div class="folder-brand">
      <div class="brand-name"><span class="brand-square"></span>TORVIK</div>
      <div class="brand-tagline">Packaging Technology</div>
    </div>
  </section>

  <section class="piece letterhead">
    <div class="letterhead-brand">
      <div class="brand-name"><span class="brand-square"></span>TORVIK</div>
      <div class="brand-tagline">Packaging Technology</div>
    </div>
    <div class="letterhead-rule"></div>
    <p class="letter-body">Dear partner, thank you for your continued trust in our filling and sealing lines. This letter confirms the schedule for the installation of the new packaging unit at your food plant next month. Our engineers will arrive on Monday morning to begin setup and safety checks. Training for your operators will follow on the second day, and full production should start by the end of the week. Please share any special hygiene rules for your site so that our team can prepare in advance. We look forward to working with you again and remain available for any question.</p>
    <footer class="letterhead-footer">
      <div class="contact-left">phone: 555 010 2040<br>&nbsp;&nbsp;&nbsp;fax: 555 010 2041<br>mobile: 555 010 2042</div>
      <div class="contact-right">web: www.torvikpack.com<br>address: 42 harbor lane, lyon, france<br>email: hello@torvikpack.com</div>
    </footer>
  </section>

  <section class="piece card-front">
    <div class="card-pattern" role="img" aria-label="Soft grey ornamental pattern on the card face"></div>
    <div class="card-front-brand">
      <div class="brand-name"><span class="brand-square"></span>TORVIK</div>
      <div class="brand-tagline">Packaging Technology</div>
    </div>
  </section>

  <section class="piece card-back">
    <div class="card-name">Lena Marsh</div>
    <div class="card-role">company director</div>
    <div class="card-contact">
      <b>web:</b> www.torvikpack.com<br>
      <b>phone:</b> 555 010 2040<br>
      <b>fax:</b> 555 010 2041<br>
      <b>email:</b> lena@torvikpack.com<br>
      <b>address:</b> 42 harbor lane, lyon
    </div>
  </section>

  <section class="piece envelope-back">
    <svg class="envelope-flap" viewBox="0 0 241 170" aria-hidden="true">
      <polyline points="0,0 120,86 241,0" fill="none" stroke="#dcdedd" stroke-width="1"/>
    </svg>
    <div class="envelope-band">
      <div class="envelope-brand">
        <div class="brand-name"><span class="brand-square"></span>TORVIK</div>
        <div class="brand-tagline">Packaging Technology</div>
      </div>
      <div class="envelope-name">Lena Marsh</div>
      <div class="envelope-role">company director</div>
    </div>
  </section>

  <section class="piece envelope-front">
    <footer class="envelope-footer">
      <div class="contact-left">phone: 555 010 2040<br>&nbsp;&nbsp;&nbsp;fax: 555 010 2041<br>mobile: 555 010 2042</div>
      <div class="contact-right">web: www.torvikpack.com<br>address: 42 harbor lane, lyon, france<br>email: hello@torvikpack.com</div>
    </footer>
  </section>

</body>
</html>
```